Changes to an existing brochure needed

We need to make some changed to an existing product brochure to add more localised information in it and to make it looks better.

We have set out in a pdf file where needs to be changed. Apart from that, any changes on the design of the brochure that can make the brochure looks better will be appreciated.

Target Market(s)

Technology market

Industry/Entity Type

Technology Equipment

Colors

Designer to choose colors to be used in the design.

Requirements
Must have
• The content outlined in the pdf file.
Nice to have
• Some creative designs that can make the brochure looks better and more professional.
Should not have
• N/A

```html
<!DOCTYPE html>
<html lang="en">
<head>
<meta charset="utf-8">
<title>Filament Materials Brochure</title>
<link href="https://fonts.googleapis.com/css2?family=Archivo+Narrow:wght@600;700&family=Arimo:ital,wght@0,400;0,700;1,700&display=swap" rel="stylesheet">
<style>
:root{
  --navy:#233a93;
  --navy-dark:#1a2c78;
  --ink:#1f3a8f;
  --paper:#ffffff;
  --swatch-frame:#e9ecf3;
}
*{box-sizing:border-box;margin:0;padding:0}
html,body{width:1200px;height:399px;overflow:hidden;background:var(--paper)}
body{font-family:"Arimo",Arial,sans-serif;color:var(--ink)}
.brochure{position:relative;width:1200px;height:399px}
.panel{position:absolute;top:0;width:384px;height:399px}
.panel--one{left:8px}.panel--two{left:408px}.panel--three{left:808px}
.material-grid{position:absolute;top:8px;left:0;width:384px;display:grid;grid-template-columns:189px 189px;grid-auto-rows:58px;gap:6px}
.material-card{position:relative;border-left:2px solid var(--navy);border-bottom:5px solid var(--navy);border-bottom-left-radius:14px;background:var(--paper)}
.material-card__title{position:absolute;top:0;right:0;left:56px;height:15px;background:var(--navy);clip-path:polygon(9px 0,100% 0,100% 100%,0 100%);color:#fff;font-family:"Archivo Narrow",Arial,sans-serif;font-weight:700;font-size:11.5px;line-height:15px;text-align:center;padding-left:8px;white-space:nowrap}
.material-card__image{position:absolute;left:4px;top:4px;width:48px;height:44px;border-radius:2px}
.material-card__points{position:absolute;left:64px;right:4px;top:18px;list-style:none;font-size:6.6px;line-height:7.4px;color:var(--ink)}
.material-card__points li{position:relative;padding-left:7px}
.material-card__points li::before{content:"";position:absolute;left:1px;top:2.2px;width:3.4px;height:3.4px;border-radius:50%;background:var(--ink)}
.material-card--teaser{background:var(--navy);border:none;border-bottom-left-radius:14px;display:flex;align-items:flex-start;justify-content:flex-end;padding:2px 6px 0 0}
.material-card--teaser span{color:#fff;font-family:"Archivo Narrow",Arial,sans-serif;font-weight:700;font-size:11.5px}
.colour-strip{position:absolute;left:0;top:328px;width:384px;height:66px;background:var(--navy);display:grid;grid-template-columns:repeat(9,1fr);gap:3px;padding:3px 3px 0}
.colour-strip--light{top:270px;height:62px;background:var(--paper)}
.swatch{display:flex;flex-direction:column;align-items:center}
.swatch__spool{width:38px;height:38px;background:var(--swatch-frame);display:flex;align-items:center;justify-content:center}
.swatch__spool i{display:block;width:30px;height:30px;border-radius:50%;box-shadow:inset 0 0 0 6px rgba(255,255,255,.35)}
.swatch__name{color:#fff;font-size:7px;line-height:7.6px;text-align:center;margin-top:3px}
.colour-strip--light .swatch__name{color:#2b2b2b}
.multicolour{position:absolute;left:0;top:338px;width:384px;text-align:center;color:var(--navy-dark)}
.multicolour__label{font-weight:700;font-style:italic;font-size:10px}
.multicolour__list{font-size:9.6px;margin-top:1px}
.contact-bar{position:absolute;left:4px;top:374px;width:376px;height:17px;border-radius:9px;background:var(--navy);color:#fff;font-weight:700;font-size:9.5px;line-height:17px;text-align:center}
</style>
</head>
<body>
<main class="brochure">

<section class="panel panel--one">
  <div class="material-grid">
    <article class="material-card"><h2 class="material-card__title">PLA / PLA+</h2><div class="material-card__image" role="img" aria-label="Printed PLA rose sample" style="background:linear-gradient(135deg,#f3c3c0,#d9716e)"></div><ul class="material-card__points"><li>Environmental-friendly material.</li><li>High print quality.</li><li>Good strength.</li></ul></article>
    <article class="material-card"><h2 class="material-card__title">xPA CF (Carbon Fibre)</h2><div class="material-card__image" role="img" aria-label="Carbon fibre printed tools" style="background:linear-gradient(135deg,#d8d8d8,#3a3a3a)"></div><ul class="material-card__points"><li>20% carbon fibre.</li><li>Highly rigid.</li><li>Good toughness and wear-resistance.</li></ul></article>
    <article class="material-card"><h2 class="material-card__title">xABS Max</h2><div class="material-card__image" role="img" aria-label="Printed jet model" style="background:linear-gradient(135deg,#eeeeee,#333)"></div><ul class="material-card__points"><li>Good temperature tolerance and creep resistance.</li><li>Flame retardant.</li></ul></article>
    <article class="material-card"><h2 class="material-card__title">ABS/ABS+</h2><div class="material-card__image" role="img" aria-label="Printed low-poly animal figure" style="background:linear-gradient(135deg,#d0d0d0,#222)"></div><ul class="material-card__points"><li>High strength.</li><li>Good toughness.</li><li>Low shrinkage for ABS+.</li></ul></article>
    <article class="material-card"><h2 class="material-card__title">PETG</h2><div class="material-card__image" role="img" aria-label="Translucent printed bells" style="background:linear-gradient(135deg,#f7e04a,#e23a3a)"></div><ul class="material-card__points"><li>Low shrinkage.</li><li>Good toughness.</li><li>High transparency and gloss.</li></ul></article>
    <article class="material-card"><h2 class="material-card__title">xASA</h2><div class="material-card__image" role="img" aria-label="Printed sports car model" style="background:linear-gradient(135deg,#f0f0f0,#1e1e1e)"></div><ul class="material-card__points"><li>Excellent mechanical property.</li><li>Outstanding UV-resistance.</li></ul></article>
    <article class="material-card"><h2 class="material-card__title">PVA</h2><div class="material-card__image" role="img" aria-label="Printed sample with soluble supports" style="background:linear-gradient(135deg,#fafafa,#e8b7b7)"></div><ul class="material-card__points"><li>Water soluble material.</li><li>Ideal for support structure.</li></ul></article>
    <article class="material-card"><h2 class="material-card__title">HIPS</h2><div class="material-card__image" role="img" aria-label="Printed patterned cat figure" style="background:linear-gradient(135deg,#f4f4f4,#3d6fc2)"></div><ul class="material-card__points"><li>Soluble in Limonence.</li><li>Works well with ABS.</li></ul></article>
    <article class="material-card"><h2 class="material-card__title">xPC</h2><div class="material-card__image" role="img" aria-label="Translucent printed vases" style="background:linear-gradient(135deg,#e6e0d6,#8a8a80)"></div><ul class="material-card__points"><li>High distortion temperature.</li><li>Low flammability.</li></ul></article>
    <article class="material-card"><h2 class="material-card__title">xPA (Nylon)</h2><div class="material-card__image" role="img" aria-label="Glowing printed lamp shade" style="background:radial-gradient(circle,#f1b43a,#2a1a08)"></div><ul class="material-card__points"><li>High toughness.</li><li>Outstanding chemical resistance.</li></ul></article>
  </div>
  <div class="colour-strip">
    <div class="swatch"><div class="swatch__spool" role="img" aria-label="White filament spool"><i style="background:#f7f7f7"></i></div><span class="swatch__name">White</span></div>
    <div class="swatch"><div class="swatch__spool" role="img" aria-label="Luminous green filament spool"><i style="background:#eef0d8"></i></div><span class="swatch__name">Luminous Green</span></div>
    <div class="swatch"><div class="swatch__spool" role="img" aria-label="Natural filament spool"><i style="background:#efe7d6"></i></div><span class="swatch__name">Natural</span></div>
    <div class="swatch"><div class="swatch__spool" role="img" aria-label="Skin filament spool"><i style="background:#f1c9a8"></i></div><span class="swatch__name">Skin</span></div>
    <div class="swatch"><div class="swatch__spool" role="img" aria-label="Yellow filament spool"><i style="background:#f5e31c"></i></div><span class="swatch__name">Yellow</span></div>
    <div class="swatch"><div class="swatch__spool" role="img" aria-label="Gold filament spool"><i style="background:#e7a73a"></i></div><span class="swatch__name">Gold</span></div>
    <div class="swatch"><div class="swatch__spool" role="img" aria-label="Orange filament spool"><i style="background:#f07a2c"></i></div><span class="swatch__name">Orange</span></div>
    <div class="swatch"><div class="swatch__spool" role="img" aria-label="Luminous red filament spool"><i style="background:#f0a0a6"></i></div><span class="swatch__name">Luminous Red</span></div>
    <div class="swatch"><div class="swatch__spool" role="img" aria-label="Luminous blue filament spool"><i style="background:#b8bcc4"></i></div><span class="swatch__name">Luminous Blue</span></div>
  </div>
</section>

<section class="panel panel--two">
  <div class="material-grid">
    <article class="material-card"><h2 class="material-card__title">xCopper</h2><div class="material-card__image" role="img" aria-label="Copper-look printed vases" style="background:linear-gradient(135deg,#e2c9b8,#9a4f2e)"></div><ul class="material-card__points"><li>Easy to process.</li><li>Metal texture after polishing.</li></ul></article>
    <article class="material-card"><h2 class="material-card__title">Bronze</h2><div class="material-card__image" role="img" aria-label="Bronze-look printed ingot" style="background:linear-gradient(135deg,#f0ead0,#a89a52)"></div><ul class="material-card__points"><li>Easy to print.</li><li>Nice shiny finish.</li></ul></article>
    <article class="material-card"><h2 class="material-card__title">xAl-fill</h2><div class="material-card__image" role="img" aria-label="Aluminium-look printed figure" style="background:linear-gradient(135deg,#dcdcdc,#6c6c6c)"></div><ul class="material-card__points"><li>Aluminium filled PLA filament.</li><li>Metal texture after polishing.</li></ul></article>
    <article class="material-card"><h2 class="material-card__title">xSteel</h2><div class="material-card__image" role="img" aria-label="Steel-look printed statue" style="background:linear-gradient(135deg,#d6d6d6,#5a5a5a)"></div><ul class="material-card__points"><li>Stainless steel filled PLA filament.</li><li>Metal texture after polishing.</li></ul></article>
    <article class="material-card"><h2 class="material-card__title">xClean</h2><div class="material-card__image" role="img" aria-label="Cleaning filament in use" style="background:linear-gradient(135deg,#f2f6fb,#5a9ad6)"></div><ul class="material-card__points"><li>Cleaning extruder before or after prints.</li><li>Wide printing temperature range.</li></ul></article>
    <article class="material-card"><h2 class="material-card__title">Color Change</h2><div class="material-card__image" role="img" aria-label="Colour changing printed model outdoors" style="background:linear-gradient(135deg,#9bbf7a,#e6a9c8)"></div><ul class="material-card__points"><li>Color changing by UV or temperature.</li><li>Reversible color change.</li></ul></article>
    <article class="material-card"><h2 class="material-card__title">Wood</h2><div class="material-card__image" role="img" aria-label="Wood-look printed sample" style="background:linear-gradient(135deg,#f3dcc1,#c69a6c)"></div><ul class="material-card__points"><li>Wood texture finish.</li><li>Low warping.</li></ul></article>
    <article class="material-card"><h2 class="material-card__title">xBamboo</h2><div class="material-card__image" role="img" aria-label="Bamboo-look printed building model" style="background:linear-gradient(135deg,#c88a63,#7a3f22)"></div><ul class="material-card__points"><li>Matte finish with dark bamboo colour.</li><li>Print with wood aroma.</li></ul></article>
    <article class="material-card"><h2 class="material-card__title">xFlex (TPU) / xLastic (TPE)</h2><div class="material-card__image" role="img" aria-label="Flexible printed insoles" style="background:linear-gradient(135deg,#9ad7c4,#2e7f8a)"></div><ul class="material-card__points"><li>High flexibility.</li><li>Good resilience.</li></ul></article>
    <article class="material-card"><h2 class="material-card__title">xTPU 95A (Not 98A)</h2><div class="material-card__image" role="img" aria-label="Flexible printed part being squeezed" style="background:linear-gradient(135deg,#ffffff,#b9b9b9)"></div><ul class="material-card__points"><li>Cost effective flexible material.</li><li>Good dimensional stability.</li></ul></article>
  </div>
  <div class="colour-strip">
    <div class="swatch"><div class="swatch__spool" role="img" aria-label="Pink filament spool"><i style="background:#f07aa0"></i></div><span class="swatch__name">Pink</span></div>
    <div class="swatch"><div class="swatch__spool" role="img" aria-label="Magenta filament spool"><i style="background:#e0326e"></i></div><span class="swatch__name">Magenta</span></div>
    <div class="swatch"><div class="swatch__spool" role="img" aria-label="Red filament spool"><i style="background:#d8232a"></i></div><span class="swatch__name">Red</span></div>
    <div class="swatch"><div class="swatch__spool" role="img" aria-label="Glass purple filament spool"><i style="background:#9a2a6a"></i></div><span class="swatch__name">Glass Purple</span></div>
    <div class="swatch"><div class="swatch__spool" role="img" aria-label="Glass lemon filament spool"><i style="background:#e6c22a"></i></div><span class="swatch__name">Glass Lemon</span></div>
    <div class="swatch"><div class="swatch__spool" role="img" aria-label="Glass orange filament spool"><i style="background:#ec8a2a"></i></div><span class="swatch__name">Glass Orange</span></div>
    <div class="swatch"><div class="swatch__spool" role="img" aria-label="Glass red filament spool"><i style="background:#b8202a"></i></div><span class="swatch__name">Glass Red</span></div>
    <div class="swatch"><div class="swatch__spool" role="img" aria-label="Purple filament spool"><i style="background:#6a3a8e"></i></div><span class="swatch__name">Purple</span></div>
    <div class="swatch"><div class="swatch__spool" role="img" aria-label="Gray filament spool"><i style="background:#8a8a8a"></i></div><span class="swatch__name">Gray</span></div>
  </div>
</section>

<section class="panel panel--three">
  <div class="material-grid">
    <article class="material-card"><h2 class="material-card__title">xSmooth</h2><div class="material-card__image" role="img" aria-label="Smooth printed ball" style="background:radial-gradient(circle,#ffffff,#c9c9c9)"></div><ul class="material-card__points"><li>Can be polished by alcohol.</li><li>Great material for metal casting.</li></ul></article>
    <article class="material-card"><h2 class="material-card__title">xMate (PCL)</h2><div class="material-card__image" role="img" aria-label="Pen-drawn printed toy figures" style="background:linear-gradient(135deg,#f6e24a,#e04a3a)"></div><ul class="material-card__points"><li>FDA approved material.</li><li>Low melting temperature.</li><li>Ideal for both 3D printer and 3D pen.</li></ul></article>
    <article class="material-card"><h2 class="material-card__title">xResin-PLA</h2><div class="material-card__image" role="img" aria-label="Red resin printed tower" style="background:linear-gradient(135deg,#ffdada,#e0202a)"></div><ul class="material-card__points"><li>Environmental-friendly.</li><li>Solidified by both UV and visible light.</li></ul></article>
    <article class="material-card"><h2 class="material-card__title">xResin- JC</h2><div class="material-card__image" role="img" aria-label="Green resin printed lattice" style="background:linear-gradient(135deg,#f4f7d0,#9ac43a)"></div><ul class="material-card__points"><li>High precision.</li><li>Smooth surface.</li><li>Ideal for metal casting.</li></ul></article>
    <article class="material-card"><h2 class="material-card__title">xResin – NC</h2><div class="material-card__image" role="img" aria-label="Orange resin printed structure" style="background:linear-gradient(135deg,#f1cfa4,#c07a3a)"></div><ul class="material-card__points"><li>Fast printing speed.</li><li>Low shrinkage.</li></ul></article>
    <article class="material-card"><h2 class="material-card__title">xResin-DC</h2><div class="material-card__image" role="img" aria-label="Dental resin printed model" style="background:linear-gradient(135deg,#d8eef2,#c98a7a)"></div><ul class="material-card__points"><li>Special designed for dental purpose.</li><li>High precision.</li><li>Good hardness.</li></ul></article>
    <article class="material-card"><h2 class="material-card__title">xPeek</h2><div class="material-card__image" role="img" aria-label="Printed boat benchmark model" style="background:linear-gradient(135deg,#f0e8e0,#c9b8a6)"></div><ul class="material-card__points"><li>Outstanding mechanical properties.</li><li>High strength, wear and fatigue resistance.</li></ul></article>
    <article class="material-card material-card--teaser"><span>Stay tuned for more materials</span></article>
  </div>
  <div class="colour-strip colour-strip--light">
    <div class="swatch"><div class="swatch__spool" role="img" aria-label="Peak green filament spool"><i style="background:#8fd48a"></i></div><span class="swatch__name">Peak Green</span></div>
    <div class="swatch"><div class="swatch__spool" role="img" aria-label="Light blue filament spool"><i style="background:#3ab8d4"></i></div><span class="swatch__name">Light Blue</span></div>
    <div class="swatch"><div class="swatch__spool" role="img" aria-label="Pine green filament spool"><i style="background:#2a8a4a"></i></div><span class="swatch__name">Pine Green</span></div>
    <div class="swatch"><div class="swatch__spool" role="img" aria-label="Green filament spool"><i style="background:#1a7a7a"></i></div><span class="swatch__name">Green</span></div>
    <div class="swatch"><div class="swatch__spool" role="img" aria-label="Blue filament spool"><i style="background:#2a3aa8"></i></div><span class="swatch__name">Blue</span></div>
    <div class="swatch"><div class="swatch__spool" role="img" aria-label="Glass light blue filament spool"><i style="background:#2a5aa8"></i></div><span class="swatch__name">Glass Light Blue</span></div>
    <div class="swatch"><div class="swatch__spool" role="img" aria-label="Brown filament spool"><i style="background:#6a3420"></i></div><span class="swatch__name">Brown</span></div>
    <div class="swatch"><div class="swatch__spool" role="img" aria-label="Black filament spool"><i style="background:#222"></i></div><span class="swatch__name">Black</span></div>
    <div class="swatch"><div class="swatch__spool" role="img" aria-label="Silver filament spool"><i style="background:#b8b8b8"></i></div><span class="swatch__name">Silver</span></div>
  </div>
  <div class="multicolour">
    <p class="multicolour__label">Multicolor Filament:</p>
    <p class="multicolour__list">PLA,PLA+,ABS,ABS+,PETG,HIPS,xMate,COLOR CHANGE,xResin Series......</p>
  </div>
  <p class="contact-bar">Please email sales@layerforge.example for more product information.</p>
</section>

</main>
</body>
</html>
```